Marlowvex Website Concept

We would like a one page website. Please refer to the attached files for more information.

Please reference file attachment version 1.1.

```html
<!DOCTYPE html>
<html lang="en">
<head>
<meta charset="utf-8">
<title>Marlowvex — Security Services</title>
<link rel="stylesheet" href="https://fonts.googleapis.com/css2?family=Open+Sans:wght@400;600;700&display=swap">
<style>
:root{
  --blue:#2a6fbf;
  --blue-dark:#1f5aa0;
  --ink:#333;
  --muted:#777;
  --line:#dcdcdc;
  --band:#ececec;
  --footer:#2c2c2c;
  --footer-bar:#1d1d1d;
  --white:#fff;
}
*{box-sizing:border-box;margin:0;padding:0}
html,body{width:796px;height:1200px;overflow:hidden;background:var(--white)}
body{font-family:"Open Sans",Arial,sans-serif;color:var(--ink);font-size:9px;line-height:1.45;position:relative}
.abs{position:absolute}
.wrap{left:120px;width:556px}

/* header */
.site-header{top:0;left:0;width:796px;height:45px;background:var(--white)}
.brand{left:120px;top:10px;display:flex;align-items:center;gap:7px;font-size:17px;font-weight:600;color:var(--ink);letter-spacing:.5px}
.brand-dot{width:22px;height:22px;border-radius:50%;background:var(--blue)}
.search{left:500px;top:12px;display:flex}
.search-field{width:150px;height:20px;background:#555;color:#ccc;font-size:8px;padding:4px 7px}
.search-btn{width:26px;height:20px;background:var(--blue);display:flex;align-items:center;justify-content:center}

/* nav */
.main-nav{top:45px;left:0;width:796px;height:27px;background:#f6f6f6;border-top:1px solid var(--line);border-bottom:1px solid var(--line)}
.main-nav ul{list-style:none;display:flex;position:absolute;left:120px;top:0;height:25px;width:556px;justify-content:space-between}
.main-nav li{font-size:8px;font-weight:600;color:#555;padding:0 12px;line-height:25px}
.main-nav li.active{background:var(--blue);color:var(--white)}

/* hero */
.hero{top:72px;left:0;width:796px;height:300px;background:linear-gradient(120deg,#e4e0da 0%,#c9c2b8 35%,#9aa4b4 65%,#d8dbe0 100%)}
.hero-caption{left:130px;top:246px;width:300px;background:rgba(20,20,20,.72);color:var(--white);padding:8px 10px}
.hero-caption h1{font-size:11px;font-weight:700;letter-spacing:.3px;margin-bottom:3px}
.hero-caption p{font-size:7.5px;color:#ddd}

/* section titles */
.section-title{font-size:11px;font-weight:700;color:var(--ink);text-transform:uppercase}

/* services */
.services{top:386px}
.service-grid{display:flex;gap:18px;margin-top:8px}
.service{width:125.5px}
.service-media{height:58px;background:linear-gradient(135deg,#8fa6bf,#4e6a8c)}
.service h3{font-size:8.5px;color:var(--blue);font-weight:600;margin:5px 0 2px}
.service p{font-size:7px;color:var(--muted);line-height:1.4}

/* welcome */
.welcome{top:600px;left:120px;width:360px}
.welcome p{font-size:7.5px;color:var(--muted);margin-top:6px;line-height:1.6}
.btn{display:inline-block;background:var(--blue);color:var(--white);font-size:7.5px;font-weight:600;padding:4px 10px;margin-top:10px}

/* consultation form */
.consult{top:600px;left:495px;width:181px;height:270px;background:var(--blue);padding:10px}
.consult h2{color:var(--white);font-size:9px;font-weight:700;text-align:center;margin-bottom:9px}
.field-row{display:flex;gap:6px;margin-bottom:6px}
.field{flex:1;height:17px;background:var(--white);font-size:6.5px;color:#999;padding:4px 5px}
.field-msg{height:58px}
.send{display:block;width:60px;margin:10px auto 0;background:var(--blue-dark);color:var(--white);text-align:center;font-size:7.5px;font-weight:700;padding:4px 0;border:1px solid #5a8fd0}

/* news */
.news{top:815px;left:120px;width:360px}
.news-head{display:flex;justify-content:space-between;align-items:center}
.news-arrows{display:flex;gap:3px}
.news-arrows span{width:11px;height:11px;background:#444;display:flex;align-items:center;justify-content:center}
.news-grid{display:flex;gap:12px;margin-top:8px}
.news-item{width:112px}
.news-media{height:52px;background:linear-gradient(135deg,#c7c1b8,#7f8a99)}
.news-item p{font-size:7.5px;color:var(--ink);margin-top:5px;line-height:1.35}

/* clients */
.clients{top:955px;left:0;width:796px;height:103px;background:var(--band)}
.clients .section-title{position:absolute;left:120px;top:12px}
.client-row{position:absolute;left:120px;top:45px;width:556px;display:flex;justify-content:space-between;align-items:center}
.client{display:flex;align-items:center;gap:5px;font-size:11px;font-weight:600;color:#9a9a9a}
.client i{width:10px;height:10px;background:#b5b5b5;display:block}

/* footer */
.site-footer{top:1058px;left:0;width:796px;height:114px;background:var(--footer);color:#ccc}
.footer-col{position:absolute;top:12px}
.footer-col h4{font-size:8.5px;color:var(--white);font-weight:600;margin-bottom:6px}
.map{width:150px;height:74px;background:linear-gradient(135deg,#d9d2c0,#b9c4a8)}
.social{list-style:none}
.social li{display:flex;align-items:center;gap:5px;font-size:7px;margin-bottom:3px}
.social li i{width:8px;height:8px;background:var(--blue);display:block}
.newsletter{font-size:7.5px;color:var(--white);margin:5px 0 3px}
.signup{display:flex}
.signup .email{width:95px;height:14px;background:var(--white);color:#999;font-size:6.5px;padding:2px 4px}
.signup .go{background:var(--blue);color:var(--white);font-size:6.5px;font-weight:700;padding:2px 6px;line-height:10px}
.contact-line{display:flex;gap:6px;align-items:flex-start;font-size:7px;margin-bottom:6px}
.contact-line svg{flex:none;margin-top:1px}

.footer-bar{top:1172px;left:0;width:796px;height:28px;background:var(--footer-bar);color:#aaa;font-size:7px}
.footer-bar .links{position:absolute;left:45px;top:9px}
.footer-bar .copy{position:absolute;right:45px;top:9px}
</style>
</head>
<body>

<header class="site-header abs">
  <div class="brand abs"><span class="brand-dot"></span>Marlowvex</div>
  <div class="search abs">
    <div class="search-field">Search...</div>
    <div class="search-btn">
      <svg width="10" height="10" viewBox="0 0 10 10"><circle cx="4" cy="4" r="3" fill="none" stroke="#fff" stroke-width="1.3"/><line x1="6.2" y1="6.2" x2="9" y2="9" stroke="#fff" stroke-width="1.4"/></svg>
    </div>
  </div>
</header>

<nav class="main-nav abs">
  <ul>
    <li class="active">HOME</li>
    <li>ABOUT US</li>
    <li>OUR SERVICES</li>
    <li>MEDIA &amp; EVENTS</li>
    <li>TRAINING</li>
    <li>BLOG</li>
    <li>CONTACT US</li>
  </ul>
</nav>

<section class="hero abs" role="img" aria-label="Photo of a smiling security consultant advising a couple at a desk">
  <div class="hero-caption abs">
    <h1>BEST SECURITY SERVICES BASED IN WASHINGTON D.C.</h1>
    <p>Trusted protection, planning and guidance for homes, offices and events across the region.</p>
  </div>
</section>

<section class="services abs wrap">
  <h2 class="section-title">Services</h2>
  <div class="service-grid">
    <article class="service">
      <div class="service-media" role="img" aria-label="Photo of a surveillance camera on a wall"></div>
      <h3>Threat Assessment</h3>
      <p>We review risks on site and report clear steps to keep your people safe.</p>
    </article>
    <article class="service">
      <div class="service-media" role="img" aria-label="Photo of network cables and a server rack"></div>
      <h3>Threat Avoidance Plan</h3>
      <p>Custom plans help your team avoid danger before it reaches your door.</p>
    </article>
    <article class="service">
      <div class="service-media" role="img" aria-label="Photo of a security officer at a control desk"></div>
      <h3>Site Executive Protection</h3>
      <p>Trained staff guard leaders and guests at offices, venues and events.</p>
    </article>
    <article class="service">
      <div class="service-media" role="img" aria-label="Photo of a technician servicing security equipment"></div>
      <h3>Secure Maintenance</h3>
      <p>Regular checks keep alarms, locks and cameras working all year long.</p>
    </article>
  </div>
</section>

<section class="welcome abs">
  <h2 class="section-title">Welcome to Marlowvex</h2>
  <p>Marlowvex is a trusted firm based in the capital that works with families, firms and public bodies to deliver calm, skilled protection. Our team brings years of field work, sharp planning and clear reporting to every job we take on. We listen first, then shape a plan that fits your site, your staff and your budget, and we stay close until the work is done. From event cover to daily patrols, we keep people safe and sites secure across the region.</p>
  <span class="btn">READ MORE</span>
</section>

<aside class="consult abs">
  <h2>REQUEST FOR CONSULTATION</h2>
  <div class="field-row"><div class="field">First Name</div><div class="field">Last Name</div></div>
  <div class="field-row"><div class="field">Email</div><div class="field">Phone</div></div>
  <div class="field-row"><div class="field">Company</div><div class="field">City</div></div>
  <div class="field-row"><div class="field">State</div><div class="field">Zip Code</div></div>
  <div class="field-row"><div class="field field-msg">Message</div></div>
  <span class="send">SEND</span>
</aside>

<section class="news abs">
  <div class="news-head">
    <h2 class="section-title">Latest News</h2>
    <div class="news-arrows">
      <span><svg width="5" height="6" viewBox="0 0 5 6"><path d="M4 0 L0 3 L4 6Z" fill="#fff"/></svg></span>
      <span><svg width="5" height="6" viewBox="0 0 5 6"><path d="M1 0 L5 3 L1 6Z" fill="#fff"/></svg></span>
    </div>
  </div>
  <div class="news-grid">
    <article class="news-item">
      <div class="news-media" role="img" aria-label="Photo of colleagues at a meeting table"></div>
      <p>Lorem ipsum dolor sit amet, consectetur amet.</p>
    </article>
    <article class="news-item">
      <div class="news-media" role="img" aria-label="Photo of a business handshake"></div>
      <p>Ut enim ad minim veniam, quis nostrud exerci.</p>
    </article>
    <article class="news-item">
      <div class="news-media" role="img" aria-label="Photo of a team reviewing documents"></div>
      <p>Duis autem vel eum iriure dolor in hendrerit in vulputate.</p>
    </article>
  </div>
</section>

<section class="clients abs">
  <h2 class="section-title">Our Clients</h2>
  <div class="client-row">
    <span class="client"><i></i>Halvern</span>
    <span class="client"><i></i>Your Logo</span>
    <span class="client"><i></i>Business</span>
    <span class="client">Brand</span>
    <span class="client"><i></i>Designer</span>
    <span class="client"><i></i>LOGO</span>
  </div>
</section>

<footer class="site-footer abs">
  <div class="footer-col" style="left:120px">
    <h4>Our Locations</h4>
    <div class="map" role="img" aria-label="Street map showing the office location"></div>
  </div>
  <div class="footer-col" style="left:325px">
    <h4>Contact Us</h4>
    <ul class="social">
      <li><i></i>Facelink</li>
      <li><i></i>Chirpline</li>
      <li><i></i>Searchplus</li>
      <li><i></i>RSS</li>
    </ul>
    <div class="newsletter">Newsletter Sign Up</div>
    <div class="signup"><span class="email">Email address</span><span class="go">SUBMIT</span></div>
  </div>
  <div class="footer-col" style="left:515px">
    <h4>Get In Touch</h4>
    <div class="contact-line">
      <svg width="8" height="8" viewBox="0 0 8 8"><path d="M1.5 0.5 L3 0.5 L3.6 2.3 L2.7 3 Q3.6 4.7 5 5.3 L5.7 4.4 L7.5 5 L7.5 6.5 Q7.5 7.5 6.5 7.5 Q0.5 7 0.5 1.5 Q0.5 0.5 1.5 0.5Z" fill="#ccc"/></svg>
      <span>+1 202 555 0147</span>
    </div>
    <div class="contact-line">
      <svg width="8" height="8" viewBox="0 0 8 8"><rect x="0.5" y="1.5" width="7" height="5" fill="none" stroke="#ccc"/><path d="M0.5 1.5 L4 4.5 L7.5 1.5" fill="none" stroke="#ccc"/></svg>
      <span>info@marlowvex.com</span>
    </div>
    <div class="contact-line">
      <svg width="8" height="9" viewBox="0 0 8 9"><path d="M4 8.5 Q0.5 5 0.5 3.5 A3.5 3.5 0 0 1 7.5 3.5 Q7.5 5 4 8.5Z" fill="#ccc"/><circle cx="4" cy="3.5" r="1.2" fill="#2c2c2c"/></svg>
      <span>123, Lorem ipsum street, Lorem ipsum<br>Lorem ipsum - 123456</span>
    </div>
  </div>
</footer>

<div class="footer-bar abs">
  <span class="links">About &nbsp;|&nbsp; Help &nbsp;|&nbsp; Contact Us &nbsp;|&nbsp; Privacy Policy &nbsp;|&nbsp; Terms of Service</span>
  <span class="copy">Copyright©2014 Marlowvex. All Rights Reserved.</span>
</div>

</body>
</html>
```